Letterhead to Prospective Clients

Create a letterhead (word & canva) that I will use to send letters to prospective clients and also include the Harbourline Estate Group Logo, My Contact Details and Interchangeable "Suburb". Use the same font and colour pallete

Maris Toppel | "Suburb" Specialist - Redlands & Surrounds
Mobile: 0417 862 905
Email: MT@HarbourlineEstateGroup.com.au

```html
<!DOCTYPE html>
<html lang="en">
<head>
<meta charset="utf-8">
<title>Harbourline Estate Group – Letterhead</title>
<link href="https://fonts.googleapis.com/css2?family=Lato:wght@400;700&family=Montserrat:wght@300;400&display=swap" rel="stylesheet">
<style>
  :root{
    --navy:#00133a;
    --navy-soft:#0a2150;
    --tan:#d8a97b;
    --ink:#111;
    --body:#666;
    --backdrop:#d3d3d3;
    --paper:#fff;
    --sig-fill:#f1f1f1;
  }
  html,body{margin:0;padding:0;width:1200px;height:1067px;overflow:hidden;background:var(--backdrop);}
  .letterhead{
    position:absolute;left:241px;top:20px;width:718px;height:1027px;
    background:var(--paper);overflow:hidden;
    box-shadow:0 6px 18px rgba(0,0,0,.18);
    font-family:'Lato',sans-serif;
  }
  .header-band{
    position:absolute;left:0;top:0;width:718px;height:150px;
    background:linear-gradient(180deg,var(--navy) 0%,var(--navy) 60%,var(--navy-soft) 100%);
  }
  .brand{position:absolute;left:56px;top:40px;color:var(--paper);font-family:'Montserrat',sans-serif;font-weight:300;}
  .brand-name{font-size:27px;letter-spacing:3px;line-height:1;}
  .brand-sub{font-size:9.5px;letter-spacing:4.2px;margin-top:9px;padding-left:2px;}
  .recipient{position:absolute;left:56px;top:281px;}
  .recipient-name{font-size:15.5px;font-weight:700;color:var(--ink);margin:0;line-height:1.2;letter-spacing:-.1px;}
  .recipient-role{font-size:11px;font-weight:700;color:var(--ink);margin:4px 0 0;}
  .letter-date{position:absolute;right:54px;top:303px;font-size:11px;color:var(--body);}
  .letter-body{position:absolute;left:57px;top:358px;width:607px;font-size:11px;line-height:17.8px;color:var(--body);text-align:justify;hyphens:auto;}
  .letter-body p{margin:0 0 17.8px;}
  .signature{position:absolute;left:56px;top:770px;width:158px;height:38px;background:var(--sig-fill);border-radius:3px;}
  .footer-rule{position:absolute;left:51px;top:945px;width:615px;height:0;border-top:1px solid var(--tan);}
  .agent{position:absolute;left:51px;top:959px;font-family:'Montserrat',sans-serif;}
  .agent-name{font-size:14px;color:var(--navy);letter-spacing:.3px;margin:0;line-height:1.2;}
  .agent-role{font-size:10.5px;color:#333;margin:3px 0 0;}
  .contact{position:absolute;right:52px;top:958px;font-family:'Montserrat',sans-serif;font-size:10.6px;color:#333;}
  .contact-row{display:flex;align-items:center;gap:5px;height:17.5px;}
  .contact-row svg{width:11px;height:9px;fill:var(--tan);}
</style>
</head>
<body>
<main class="letterhead">
  <div class="header-band" role="img" aria-label="Decorative navy header with flowing navy and gold wave ribbons"></div>
  <div class="brand">
    <div class="brand-name">HARBOURLINE</div>
    <div class="brand-sub">ESTATE GROUP</div>
  </div>

  <div class="recipient">
    <p class="recipient-name">Dear. Mrs Elena Rose Whitby</p>
    <p class="recipient-role">Chief Director</p>
  </div>
  <div class="letter-date">Date: 17-June-2025</div>

  <div class="letter-body">
    <p>Lorem ipsum dolor sit amet, consectetur adipiscing elit, sed do eiusmod tempor incididunt ut labore et dolore magna aliqua. Sollicitudin ac orci phasellus egestas tellus rutrum tellus. Euismod elementum nisi quis eleifend quam adipiscing vitae proin sagittis. Egestas sed tempus urna et pharetra pharetra. Quis blandit turpis cursus in hac habitasse. Sed velit dignissim sodales ut eu. Ac auctor augue mauris augue neque. In arcu cursus euismod quis viverra nibh cras pulvinar mattis. Libero justo laoreet sit amet. Felis eget nunc lobortis mattis aliquam faucibus purus in. Pulvinar etiam non quam lacus suspendisse faucibus. Odio tempor orci dapibus ultrices. Velit dignissim sodales ut eu sem integer vitae justo. Fermentum et sollicitudin ac orci phasellus egestas. Pharetra vel turpis nunc eget lorem dolor sed. Sed turpis tincidunt id aliquet risus feugiat in ante. Mus mauris vitae ultricies leo integer malesuada nunc vel. Rhoncus urna neque viverra justo nec ultrices dui. Ut placerat orci nulla pellentesque dignissim enim sit amet.</p>
    <p>Bibendum arcu vitae elementum curabitur vitae nunc. Nunc pulvinar sapien et ligula ullamcorper malesuada. At elementum eu facilisis sed. Erat pellentesque adipiscing commodo elit at imperdiet dui accumsan sit. Nunc scelerisque viverra mauris in aliquam sem fringilla. In vitae turpis massa sed. Volutpat ac tincidunt vitae semper quis lectus nulla at. Massa placerat duis ultricies lacus sed turpis. Dui vivamus arcu felis bibendum ut tristique et egestas. Blandit aliquam etiam erat velit scelerisque in dictum non consectetur. Id neque aliquam vestibulum morbi blandit cursus risus at. Sed egestas egestas fringilla phasellus faucibus scelerisque eleifend donec. Ornare quam viverra orci sagittis eu volutpat odio facilisis. Volutpat sed cras ornare arcu dui vivamus arcu. Interdum consectetur libero id faucibus nisl.</p>
    <p>Viverra mauris in aliquam sem. Mattis molestie a iaculis at erat pellentesque adipiscing commodo elit. Sit amet volutpat consequat mauris nunc. Aliquam nulla facilisi cras fermentum. Sed turpis tincidunt id aliquet risus feugiat. Augue neque gravida in fermentum et sollicitudin ac orci.</p>
  </div>

  <div class="signature" role="img" aria-label="Handwritten signature of the sender"></div>

  <div class="footer-rule"></div>
  <div class="agent">
    <p class="agent-name">MARIS TOPPEL</p>
    <p class="agent-role">Specialist - Redlands &amp; Surrounds</p>
  </div>
  <div class="contact">
    <div class="contact-row">
      <svg viewBox="0 0 12 10" aria-hidden="true"><path d="M1,3 C1,1 3,0.5 6,0.5 C9,0.5 11,1 11,3 L9,3.5 L8.5,2.3 H3.5 L3,3.5 Z M3,4 H9 L10.5,9.5 H1.5 Z"/></svg>
      <span>0417 862 905</span>
    </div>
    <div class="contact-row">
      <svg viewBox="0 0 12 10" aria-hidden="true"><path d="M0.5,1 H11.5 L6,5.5 Z M0.5,2.2 L6,6.8 L11.5,2.2 V9 H0.5 Z"/></svg>
      <span>MT@HarbourlineEstateGroup.com.au</span>
    </div>
  </div>
</main>
</body>
</html>
```